Mr. Tovrin Beard Oil labels for 2oz bottle and a label for its box

I am looking to design a label for a 2oz beard oil glass bottle as well as its box. This is for a new company so the design should be high fidelity and captivating. Ideally I would like a picture on the bottle of a mans face at a 45 degree angle. His beard will be curly/course and full. Something like the uploaded file in a fuller more detailed way (Without the beanie), he can be bald. The characters mouth does not necessarily have to be opened and should not be Marcus Dellow since I don't have rights to use his photo on a product. I'm looking to use earthy tones for the bottle label and box that bleeds sophistication with a modern urban hint to it. The product will boast a perfect blend of 6 key oils that work best for hair follicles that struggle to retain moisture. Leaving it soft and moisturized without an unpleasant smell.

Back label of box should read:

Beard care has been passed down for generations and is only now becoming a popular trend. Mr. Tovrin’s beard products formulated for tightly coiled and kinky hair, has mastered the science over the years, to bring you a specifically refined product that is guaranteed to let the mane reign!

With a proper washing routine, Mr. Tovrin beard oil is guaranteed to leave your beard moisturized, itch and dandruff free without any chemicals. Mr. Tovrins oil mixture is 100% natural and organic, so you know you're getting the best. Mr. Tovrin’s beard oil is uniquely different for a unique difference.

"The essence of a mans style is what he puts on, so it better be Tovrin"

Target Market(s)

African Americans and Individuals with hair follicles that do not retain much moisture.

Industry/Entity Type

Hair And Beauty

Font styles to use
Decorative
Script

Colors
000000
757575
f37122
faa54b
f78f20
ec1f27
9bcb3b
ffffff

Requirements
Must have
• A captivating character (Vector File) on the front of the bottle that has a kinky, curly beard. I would like the character to resemble the cartoonish style features of the copper vale character I included in the attached picture, however make him look more black (African American)
• Also the box rear label needs to have the descriptive last 2 paragraphs I included in the project description. The last sentence "The essence of a mans style is what he puts on, so it better be Tovrin" should be at the very bottom of the box front or back, whichever looks best.
• Main colors are tan (Label base), black (lettering), Red (Slight accenting), the rest is up to you. I want the label to have primarily earth tones, brown, tan, green.
Nice to have
• Mr. Tovrin Beard Oil lettering would preferably be in black, with a thin outlining of Red. As for the bottle I would prefer it be a tan label with black and grey lettering with very slight accenting of any color you think would look best with my design. The colors I chose below are just guidelines, except for the shades of tan. I would like the box to incorporate a shade of tan with the other colors making up the designs and letters
Should not have
• Label lettering on back of box should not be in script. Script should not be too distracting. The red should not overpower the labels at all. Almost none existent yet noticeable. The brighter colors should not make up more than 20% of the label

```html
<!DOCTYPE html>
<html lang="en">
<head>
<meta charset="utf-8">
<title>Mr. Tovrin Beard Oil — Label Set</title>
<link rel="stylesheet" href="https://fonts.googleapis.com/css2?family=Crimson+Text:wght@400;700&display=swap">
<style>
  :root {
    --page: #f4f1ec;
    --tan-light: #f3dfb0;
    --tan: #e9cd93;
    --tan-deep: #d9b677;
    --tan-edge: #cbb68c;
    --ink: #000000;
    --ink-soft: #1a1a1a;
    --band: #0d0a08;
    --quote: #e0803c;
    --stripe: #e0a060;
    --art-dark: #6f6658;
    --art-light: #d8cdb6;
  }
  * { box-sizing: border-box; margin: 0; padding: 0; }
  html, body { width: 941px; height: 1200px; overflow: hidden; }
  body {
    background: var(--page);
    font-family: "Crimson Text", Georgia, serif;
    color: var(--ink);
    position: relative;
  }

  /* ---------- Box back label ---------- */
  .box-back {
    position: absolute;
    left: 58px; top: 330px;
    width: 380px; height: 560px;
    background: var(--tan-edge);
    padding: 8px 10px 24px;
  }
  .box-back__panel {
    position: relative;
    width: 100%; height: 100%;
    background: radial-gradient(ellipse at 40% 40%, var(--tan-light), var(--tan) 60%, var(--tan-deep));
    padding: 36px 26px 30px;
  }
  .box-back__frame { position: absolute; inset: 0; width: 100%; height: 100%; }
  .box-back__name {
    position: relative;
    text-align: center;
    font-weight: 700;
    font-size: 21px;
    letter-spacing: 1.5px;
    text-transform: uppercase;
    margin-bottom: 4px;
  }
  .box-back__copy {
    position: relative;
    font-size: 16.2px;
    line-height: 1.2;
    color: var(--ink-soft);
  }
  .box-back__copy p + p { margin-top: 20px; }
  .drop-cap {
    float: left;
    font-size: 50px;
    line-height: 0.8;
    margin: 4px 3px 0 0;
  }

  /* ---------- Bottle front label ---------- */
  .bottle-front {
    position: absolute;
    left: 498px; top: 330px;
    width: 360px; height: 560px;
  }
  .bottle-front__panel {
    position: absolute;
    left: 0; top: 0;
    width: 360px; height: 500px;
    background: radial-gradient(ellipse at 50% 35%, var(--tan-light), var(--tan) 60%, var(--tan-deep));
  }
  .bottle-front__frame { position: absolute; inset: 0; width: 100%; height: 100%; }
  .bottle-front__name {
    position: absolute;
    left: 0; right: 0; top: 38px;
    text-align: center;
    font-weight: 700;
    font-size: 36px;
    letter-spacing: 2px;
    text-transform: uppercase;
    line-height: 1;
  }
  .bottle-front__variant {
    position: absolute;
    left: 0; right: 0; top: 82px;
    text-align: center;
    font-weight: 700;
    font-size: 30px;
    letter-spacing: 6px;
  }
  .bottle-front__art {
    position: absolute;
    left: 80px; top: 126px;
    width: 200px; height: 330px;
    border-radius: 46% 46% 48% 48% / 30% 30% 62% 62%;
    background: radial-gradient(ellipse at 50% 45%, var(--art-light), var(--art-dark) 85%);
    opacity: 0.85;
  }
  .bottle-front__quote {
    position: absolute;
    left: 0; top: 466px;
    width: 360px; height: 68px;
    background: var(--band);
    border-radius: 14px;
    color: var(--quote);
    font-size: 17px;
    line-height: 1.1;
    text-align: center;
    display: flex; align-items: center; justify-content: center;
    padding: 0 8px;
  }
  .bottle-front__stripe {
    position: absolute;
    left: 0; top: 536px;
    width: 360px; height: 8px;
    background: var(--stripe);
  }
</style>
</head>
<body>

  <section class="box-back" aria-label="Box back label">
    <div class="box-back__panel">
      <svg class="box-back__frame" viewBox="0 0 360 528" preserveAspectRatio="none" aria-hidden="true">
        <g stroke="#000" fill="none">
          <line x1="6" y1="8" x2="354" y2="8" stroke-width="3"/>
          <line x1="16" y1="16" x2="344" y2="16" stroke-width="1.5"/>
          <line x1="6" y1="520" x2="354" y2="520" stroke-width="3"/>
          <line x1="16" y1="512" x2="344" y2="512" stroke-width="1.5"/>
          <line x1="8" y1="8" x2="8" y2="520" stroke-width="2"/>
          <line x1="352" y1="8" x2="352" y2="520" stroke-width="2"/>
        </g>
      </svg>
      <h1 class="box-back__name">Mr Tovrin Beard</h1>
      <div class="box-back__copy">
        <p><span class="drop-cap">B</span>eard care has been passed down for generations and is only now becoming a popular trend. Mr. Tovrin’s beard products formulated for tightly coiled and kinky hair, has mastered the science over the years, to bring you a specifically refined product that is guaranteed to let the mane reign!</p>
        <p>With a proper washing routine, Mr. Tovrin beard oil is guaranteed to leave your beard moisturized, itch and dandruff free without any chemicals. Mr. Tovrins oil mixture is 100% natural and organic, so you know you're getting the best. Mr. Tovrin’s beard oil is uniquely different for a unique difference.</p>
      </div>
    </div>
  </section>

  <section class="bottle-front" aria-label="Bottle front label">
    <div class="bottle-front__panel">
      <svg class="bottle-front__frame" viewBox="0 0 360 500" aria-hidden="true">
        <g stroke="#000" fill="none">
          <line x1="92" y1="98" x2="150" y2="98" stroke-width="2"/>
          <line x1="92" y1="104" x2="150" y2="104" stroke-width="1"/>
          <line x1="210" y1="98" x2="268" y2="98" stroke-width="2"/>
          <line x1="210" y1="104" x2="268" y2="104" stroke-width="1"/>
          <line x1="20" y1="120" x2="20" y2="470" stroke-width="3"/>
          <line x1="340" y1="120" x2="340" y2="470" stroke-width="3"/>
        </g>
      </svg>
      <h2 class="bottle-front__name">Mr Tovrin Beard</h2>
      <div class="bottle-front__variant">OIL</div>
      <div class="bottle-front__art" role="img" aria-label="Illustration of a bearded man with a full curly beard, smoking a pipe"></div>
    </div>
    <p class="bottle-front__quote">"The essence of a mans style<br>is what he puts on, so it better be Tovrin"</p>
    <div class="bottle-front__stripe"></div>
  </section>

</body>
</html>
```